Create the ONLY Supplement line for Male Entrepreneurs! (Veltro Prime MD)

I need a label designed for a new supplement brand that I am launching.

There are five products so need a design that I can simply change the wording for each individual product

The brand name is called veltro prime MD. The focus is male entrepreneurial health.

Target audience is men 35 to 55.

Concepts: the healthier you are in body the more money you will make in business.

Concept to copy: I want to make a clean minimalistic label mimicking Dallamore MD (google it and you'll see what I mean)

Target Market(s)

male entrepreneurs 35-55

Industry/Entity Type

Health Supplement

Colors

Designer to choose colors to be used in the design.

Requirements
Must have
• Modern classy design, similar to Dallamore MD.
Nice to have
• Highlight that the supplement is Doctor Approved.
Should not have
• No loud colors. Present it as high class.

```html
<!DOCTYPE html>
<html lang="en">
<head>
<meta charset="utf-8">
<title>Veltro Prime MD – Omega 3 Label</title>
<link href="https://fonts.googleapis.com/css2?family=Abel&family=Libre+Franklin:wght@400;700;900&display=swap" rel="stylesheet">
<style>
  :root {
    --stage: #e6e7e8;
    --label: #ffffff;
    --ink: #333335;
    --ink-dark: #3a3a3c;
    --band-text: #f2f2f2;
    --rule: #222222;
  }
  * { box-sizing: border-box; margin: 0; padding: 0; }
  html, body { width: 1200px; height: 658px; overflow: hidden; background: var(--stage); }
  .canvas { position: relative; width: 1200px; height: 658px; }
  .label {
    position: absolute; left: 66px; top: 15px; width: 1068px; height: 628px;
    background: var(--label); color: var(--ink);
    font-family: "Abel", sans-serif;
  }
  .copy {
    position: absolute; left: 52px; top: 130px; width: 235px;
    font-size: 16.5px; line-height: 20.4px; text-align: justify; letter-spacing: -0.2px;
  }
  .copy p + p { margin-top: 20px; }
  .info-panel {
    position: absolute; left: 52px; top: 438px; width: 161px; height: 79px;
    background: var(--ink-dark);
  }
  .brand { position: absolute; left: 397px; top: 62px; width: 273px; }
  .brand-name { font-size: 47px; line-height: 56px; letter-spacing: -1.2px; white-space: nowrap; }
  .brand-rule { height: 1.5px; background: var(--ink); margin-top: 10px; }
  .brand-sub { display: flex; justify-content: space-between; align-items: center; margin-top: 4px; }
  .brand-sub span { font-size: 30px; line-height: 36px; }
  .brand-mark { width: 22px; height: 22px; border-radius: 50%; background: var(--ink-dark); margin-right: 4px; }
  .product-name {
    position: absolute; left: 395px; top: 398px;
    font-size: 60px; line-height: 70px; letter-spacing: -1px;
  }
  .potency-band {
    position: absolute; left: 366px; top: 472px; width: 334px; height: 52px;
    background: var(--ink-dark); color: var(--band-text);
    font-size: 32px; line-height: 52px; padding-left: 37px;
  }
  .volume { position: absolute; left: 395px; top: 526px; font-size: 36px; line-height: 42px; letter-spacing: -0.5px; }

  .nutrition {
    position: absolute; left: 800px; top: 131px; width: 216px;
    border: 1px solid var(--rule); padding: 3px 4px 4px;
    font-family: "Libre Franklin", sans-serif; color: #111;
  }
  .nf-title { font-weight: 900; font-size: 25px; line-height: 27px; letter-spacing: -0.4px; }
  .nf-thin { border-top: 1px solid var(--rule); }
  .nf-thick { height: 8px; background: var(--rule); }
  .nf-mid { height: 4px; background: var(--rule); }
  .nf-small { font-size: 11px; line-height: 14px; }
  .nf-row { display: flex; justify-content: space-between; font-size: 10px; line-height: 14.3px; border-top: 1px solid var(--rule); }
  .nf-row.first { border-top: 0; }
  .nf-row b { font-weight: 700; }
  .nf-serving { display: flex; justify-content: space-between; font-weight: 700; font-size: 12.5px; line-height: 15px; margin-bottom: 2px; }
  .nf-amount { font-size: 7px; font-weight: 700; line-height: 9px; margin-top: 4px; }
  .nf-calories { display: flex; justify-content: space-between; font-weight: 900; line-height: 24px; margin-bottom: 2px; }
  .nf-calories span:first-child { font-size: 20px; }
  .nf-calories span:last-child { font-size: 26px; }
  .nf-dv { font-size: 7px; font-weight: 700; text-align: right; line-height: 12px; }
  .ind1 { padding-left: 14px; }
  .ind2 { padding-left: 28px; }
  .nf-foot { font-size: 7.5px; line-height: 9.5px; padding: 3px 2px 0 4px; }
</style>
</head>
<body>
<div class="canvas">
  <section class="label">
    <div class="copy">
      <p>Lorem ipsum dolor sit amet, consectetuer adipiscing elit, sed diam nonummy nibh euismod tincidunt ut laoreet dolore magna aliquam erat volutpat.</p>
      <p>Ut wisi enim ad minim veniam, Lorem ipsum dolor sit amet, consectetuer adipiscing elit, sed diam nonummy nibh euismod tincidunt ut laoreet dolore magna aliquam erat volutpat. Ut wisi enim ad minim veniam.</p>
    </div>
    <div class="info-panel"></div>

    <div class="brand">
      <div class="brand-name">veltro prime MD</div>
      <div class="brand-rule"></div>
      <div class="brand-sub"><span>supplement</span><i class="brand-mark"></i></div>
    </div>

    <div class="product-name">Omega 3</div>
    <div class="potency-band">HIGH POTENCY</div>
    <div class="volume">59 ml / 2fl oz</div>

    <div class="nutrition">
      <div class="nf-title">Nutrition Facts</div>
      <div class="nf-thin"></div>
      <div class="nf-small">4 servings per container</div>
      <div class="nf-serving"><span>Serving size</span><span>1 cup (180g)</span></div>
      <div class="nf-thick"></div>
      <div class="nf-amount">Amount per serving</div>
      <div class="nf-calories"><span>Calories</span><span>245</span></div>
      <div class="nf-mid"></div>
      <div class="nf-dv">% Daily Value*</div>
      <div class="nf-row"><span><b>Total Fat</b> 12g</span><b>14%</b></div>
      <div class="nf-row"><span class="ind1">Saturated Fat 2g</span><b>10%</b></div>
      <div class="nf-row"><span class="ind1"><i>Trans</i> Fat 0g</span><span></span></div>
      <div class="nf-row"><span><b>Cholesterol</b> 8mg</span><b>3%</b></div>
      <div class="nf-row"><span><b>Sodium</b> 210mg</span><b>9%</b></div>
      <div class="nf-row"><span><b>Total Carbohydrate</b> 34g</span><b>12%</b></div>
      <div class="nf-row"><span class="ind1">Dietary Fiber 7g</span><b>25%</b></div>
      <div class="nf-row"><span class="ind1">Total Sugars 5g</span><span></span></div>
      <div class="nf-row"><span class="ind2">Includes 4g Added Sugars</span><b>8%</b></div>
      <div class="nf-row"><span><b>Protein</b> 11g</span><span></span></div>
      <div class="nf-thick"></div>
      <div class="nf-row first"><span>Vit. D 4mcg 20%</span><span>·</span><span>Calcium 210mg 16%</span></div>
      <div class="nf-row"><span>Iron 3mg 15%</span><span>·</span><span>Potas. 380mg 8%</span></div>
      <div class="nf-row"><span>Vit. A 84mcg 9%</span><span>·</span><span>Vit. C 10mg 11%</span></div>
      <div class="nf-row"><span>Zinc 7mg 17%</span><span>·</span><span>Iodine 15mcg 10%</span></div>
      <div class="nf-mid"></div>
      <div class="nf-foot">* The % Daily Value (DV) tells you how much a nutrient in a serving of food contributes to a daily diet. 2,000 calories a day is used for general nutrition advice.</div>
    </div>
  </section>
</div>
</body>
</html>
```